Nutritional neuroscience book cover design*

We need a book cover design for a new book on nutritional neuroscience and aging. The book is written for the general public and answers questions such as, "We are living longer than ever. The problem is, will our brain stay healthy as we age? We certainly do not want to live longer with various diseases, in particular brain diseases. How does the brain change during aging? And what can we do to promote the health of our brain and prevent and treat neurological diseases that typically occur during the aging process?" Based on recent discoveries in the field of nutritional neuroscience, this book presents how we can use nutrition to help our brain stay healthy longer. While our brain shrinks and becomes functionally weaker during the aging process, nutrition is able to slow this process down. This book illustrates this point through chapters on stroke, Parkinson’s disease, Multiple Sclerosis, dementia, depression, anxiety, and schizophrenia. The book will appeal to anyone looking to optimize their brain’s health and performance today and decades into the future.

Target Market(s)

General audience

Colors

Designer to choose colors to be used in the design.

Requirements
Must have
• Title: Meals Across the Decades: A Companion Guide to Dietary Brain Science Today
• Edited by Odelia R. Vantrosk, Ph.D.
• Book size: 7*10 inches
• Backcover text:
• Humans are living longer than ever. How does the brain change during aging? Will our brain stay healthy as we age? We certainly do not want to live longer with neurological diseases. What can we do to promote the health of our brain?
• Based on recent discoveries in the field of nutritional neuroscience, this book presents how nutrition affects our brain health. While we age, our brain shrinks and there are changes in how it functions, nutrition is an important component that can help maintain optimal brain health.
• Using scientific evidence, this book illustrates the importance of nutrition for neurological diseases including Alzheimer’s disease, stroke, Parkinson’s disease, Multiple Sclerosis, vascular dementia, depression, anxiety, and schizophrenia. This book will appeal to anyone looking to learn more about how nutrition affects brain health.

```html
<!DOCTYPE html>
<html lang="en">
<head>
<meta charset="utf-8">
<title>Meals Across the Decades – Cover Spread</title>
<link href="https://fonts.googleapis.com/css2?family=Questrial&family=Tinos&display=swap" rel="stylesheet">
<style>
  :root {
    --page-bg: #f6f4f5;
    --paper-white: #ffffff;
    --cover-yellow: #ffff00;
    --soft-yellow: #ffff66;
    --accent-red: #ed1c24;
    --title-red: #ff0000;
    --title-olive: #4d4d1a;
    --subtitle-green: #4a561c;
    --ink: #111111;
    --orange: #f7941d;
    --cyan: #00ffff;
    --light-green: #a5d16f;
    --navy: #1b1464;
    --leaf: #3aaa35;
    --dark-olive: #556b1e;
    --pink: #ee2a9b;
    --coral: #f04e23;
    --frame-grey: #9a9a9a;
  }
  html, body {
    margin: 0;
    width: 1200px;
    height: 806px;
    overflow: hidden;
    background: var(--page-bg);
  }
  .spread { display: block; width: 1200px; height: 806px; }
  .sans { font-family: "Questrial", sans-serif; }
  .serif { font-family: "Tinos", serif; }
  .back-heading { fill: var(--paper-white); font-size: 30px; }
  .blurb { fill: var(--paper-white); font-size: 17px; }
  .bio { fill: var(--ink); font-size: 15px; }
  .pic-label { fill: var(--ink); font-size: 15px; }
  .spine-text { fill: var(--title-olive); font-size: 13px; }
  .title-lead { fill: var(--title-olive); font-size: 44px; }
  .title-main { fill: var(--title-red); font-size: 140px; }
  .title-tail { fill: var(--subtitle-green); font-size: 58px; }
  .subtitle { fill: var(--title-red); font-style: italic; }
  .subtitle-small { font-size: 30px; }
  .subtitle-large { font-size: 46px; }
  .edited-by { fill: var(--ink); font-size: 21px; }
  .editor-name { fill: var(--ink); font-size: 70px; }
</style>
</head>
<body>
<svg class="spread" viewBox="0 0 1488 1000" xmlns="http://www.w3.org/2000/svg">
  <defs>
    <linearGradient id="coverFade" x1="0" y1="0" x2="0" y2="1">
      <stop offset="0" stop-color="var(--paper-white)"/>
      <stop offset="0.5" stop-color="var(--paper-white)"/>
      <stop offset="0.72" stop-color="var(--soft-yellow)"/>
      <stop offset="1" stop-color="var(--cover-yellow)"/>
    </linearGradient>
    <linearGradient id="portraitTone" x1="0" y1="0" x2="0" y2="1">
      <stop offset="0" stop-color="#eef2f6"/>
      <stop offset="0.6" stop-color="#f3ecc8"/>
      <stop offset="1" stop-color="#f8f49a"/>
    </linearGradient>
  </defs>

  <!-- Cover spread -->
  <rect class="cover" x="84" y="30" width="1338" height="947" fill="url(#coverFade)"/>

  <!-- Back cover -->
  <g class="back-cover">
    <circle cx="418" cy="375" r="314" fill="var(--accent-red)"/>
    <text class="sans back-heading" x="401" y="126" text-anchor="middle">About the Book</text>
    <g class="sans blurb" text-anchor="middle">
      <text x="420" y="210">Lorem ipsum dolor sit amet, consectetur adipiscing elit, sed do</text>
      <text x="420" y="232">eiusmod tempor incididunt ut labore et dolore magna aliqua. Quis</text>
      <text x="420" y="254">ipsum suspendisse ultrices gravida. Risus commodo viverra maecenas</text>
      <text x="420" y="276">accumsan lacus vel facilisis.</text>
      <text x="420" y="318">Lorem ipsum dolor sit amet, consectetur adipiscing elit, sed do</text>
      <text x="420" y="340">eiusmod tempor incididunt ut labore et dolore magna aliqua. Quis</text>
      <text x="420" y="362">ipsum suspendisse ultrices gravida. Risus commodo viverra maecenas</text>
      <text x="420" y="384">accumsan lacus vel facilisis.</text>
      <text x="420" y="435">Lorem ipsum dolor sit amet, consectetur adipiscing</text>
      <text x="420" y="457">elit, sed do eiusmod tempor incididunt ut labore et</text>
      <text x="420" y="479">dolore magna aliqua. Quis ipsum suspendisse ultrices</text>
      <text x="420" y="501">gravida. Risus commodo viverra maecenas</text>
      <text x="420" y="523">accumsan lacus vel facilisis.</text>
    </g>
    <circle cx="183" cy="533" r="12" fill="var(--cyan)"/>
    <circle cx="352" cy="550" r="18" fill="var(--cover-yellow)"/>
    <circle cx="226" cy="653" r="23" fill="var(--light-green)"/>
    <circle cx="474" cy="673" r="52" fill="var(--orange)"/>
    <circle cx="578" cy="685" r="31" fill="var(--navy)"/>

    <g class="author-panel">
      <rect x="119" y="708" width="411" height="222" fill="var(--cover-yellow)"/>
      <rect x="144" y="735" width="353" height="173" fill="var(--paper-white)"/>
      <rect x="162" y="746" width="106" height="144" fill="var(--paper-white)" stroke="var(--frame-grey)" stroke-width="1.5"/>
      <text class="sans pic-label" x="215" y="821" text-anchor="middle">authur pic</text>
      <g class="sans bio">
        <text x="286" y="769">Lorem ipsum dolor sit amet,</text>
        <text x="286" y="788">consectetur adipiscing elit,</text>
        <text x="286" y="806">sed do eiusmod tempor</text>
        <text x="286" y="825">incididunt ut labore et</text>
        <text x="286" y="843">dolore magna aliqua. Quis</text>
        <text x="286" y="862">ipsum suspendisse ultrices</text>
        <text x="286" y="880">gravida. Risus commodo</text>
      </g>
    </g>
    <rect class="code-space" x="548" y="836" width="167" height="132" fill="var(--paper-white)"/>
  </g>

  <!-- Spine -->
  <g class="spine sans spine-text">
    <text transform="translate(748 70) rotate(90)">Meals Across the Decades</text>
    <text transform="translate(748 306) rotate(90)">Edited by</text>
    <text transform="translate(748 378) rotate(90)">Odelia R. Vantrosk</text>
  </g>

  <!-- Front cover -->
  <g class="front-cover">
    <rect x="830" y="345" width="490" height="540" rx="210" fill="url(#portraitTone)" role="img" aria-label="Side profile photograph of an older man's head inside a blue-to-yellow head outline"/>
    <circle cx="844" cy="270" r="19" fill="var(--orange)"/>
    <circle cx="933" cy="318" r="52" fill="var(--cyan)"/>
    <circle cx="802" cy="370" r="23" fill="var(--light-green)"/>
    <circle cx="836" cy="441" r="18" fill="var(--dark-olive)"/>
    <circle cx="985" cy="535" r="115" fill="var(--coral)" opacity="0.88"/>
    <circle cx="1072" cy="416" r="79" fill="var(--leaf)" opacity="0.85"/>
    <circle cx="975" cy="418" r="17" fill="var(--navy)"/>
    <circle cx="906" cy="430" r="63" fill="#ffee00" opacity="0.9"/>
    <circle cx="870" cy="596" r="52" fill="var(--pink)" opacity="0.8"/>

    <text class="sans title-lead" x="1048" y="100" text-anchor="middle">Meals Across the</text>
    <text class="serif title-main" x="1090" y="213" text-anchor="middle">Decades</text>
    <text class="sans title-tail" x="965" y="308" textLength="400" lengthAdjust="spacingAndGlyphs">A Companion Guide</text>

    <text class="sans subtitle subtitle-small" x="880" y="745">to Dietary Brain</text>
    <text class="sans subtitle subtitle-large" x="805" y="806">Science Today</text>

    <text class="sans edited-by" x="847" y="880">Edited by</text>
    <text class="sans editor-name" x="815" y="955" textLength="563" lengthAdjust="spacingAndGlyphs">Odelia R. Vantrosk</text>
  </g>
</svg>
</body>
</html>
```